Tiko Marsden Systems Web Site

I need website designed for Tiko Marsden Systems, LLC. It is an email marketing software as a service business. I am looking for a five page website with the ability to accept payments. I have included our logo below for integration with the website. I do not have the text ready yet.

The domain to use is tiko-marsden.example

I have also included some examples of other websites that outline the basic structure I would like
https://trybluvoren.example/
https://www.postquill.example/

I know I need to provide some more information, but I want to get the ball rolling and see what is needed.
Thanks!
Owen

```html
<!DOCTYPE html>
<html lang="en">
<head>
<meta charset="utf-8">
<title>Tiko Marsden Systems — Email Marketing Software</title>
<link rel="stylesheet" href="https://fonts.googleapis.com/css2?family=Poppins:wght@300;400;500;600;700&display=swap">
<style>
:root{
  --red:#f2232b;
  --navy:#231d63;
  --ink:#333333;
  --grey:#777777;
  --muted:#9a9a9a;
  --hero-deep:#0e1f33;
  --hero-mid:#29445f;
  --band:#e9eaeb;
  --footer:#f4f4f4;
  --white:#ffffff;
  --brand:#2c8fc8;
}
*{box-sizing:border-box;margin:0;padding:0}
html,body{width:1200px;height:2525px;overflow:hidden}
body{position:relative;background:var(--white);font-family:"Poppins",sans-serif;color:var(--ink)}
.abs{position:absolute}

/* Header */
.site-header{left:0;top:0;width:1200px;height:96px;background:rgba(245,246,248,.96);z-index:3}
.brand{left:135px;top:28px;display:flex;align-items:center;gap:10px}
.brand-mark{width:40px;height:40px;border-radius:50%;border:2px solid var(--brand)}
.brand-name{font-size:19px;font-weight:500;color:var(--brand);letter-spacing:.5px}
.main-nav a{position:absolute;top:39px;font-size:13.5px;font-weight:400;color:#222;text-decoration:none;letter-spacing:.4px}
.btn{display:flex;align-items:center;justify-content:center;background:var(--red);color:var(--white);text-decoration:none;font-weight:500;border-radius:3px}
.btn-signup{left:976px;top:30px;width:89px;height:36px;font-size:12.5px}

/* Hero */
.hero{left:0;top:96px;width:1200px;height:535px;background:linear-gradient(100deg,var(--hero-deep) 0%,#1a3048 40%,var(--hero-mid) 70%,#6d7c8a 100%)}
.hero-title{left:131px;top:200px;font-size:47px;font-weight:700;line-height:54px;color:var(--white)}
.hero-tagline{left:131px;top:315px;font-size:32px;font-weight:400;color:var(--white)}
.hero-sub{left:131px;top:363px;font-size:21px;font-weight:400;color:var(--white)}
.btn-pricing{left:131px;top:429px;width:202px;height:37px;font-size:14px}

/* Intro */
.intro-title{left:0;top:682px;width:1200px;text-align:center;font-size:32px;font-weight:400;color:var(--navy)}
.intro-text{left:0;top:730px;width:1200px;text-align:center;font-size:24px;font-weight:300;line-height:28px;color:var(--muted)}

.feature{width:330px;text-align:center}
.feature-art{width:130px;height:126px;margin:0 auto;border-radius:50%}
.feature h3{font-size:19px;font-weight:400;color:var(--ink);margin-top:40px}
.feature p{font-size:12.5px;line-height:15px;color:var(--muted);margin:22px auto 0;width:270px}

/* Developers */
.dev-title{left:133px;top:1220px;font-size:32px;font-weight:600;line-height:37px;color:#3a3a3a}
.dev-photo{left:577px;top:1202px;width:488px;height:523px;background:linear-gradient(135deg,#cfd3d4 0%,#8f9aa0 35%,#3d4a52 55%,#d8c7a8 80%,#efe7da 100%)}
.dev-card{left:114px;top:1330px;width:520px;height:434px;background:var(--white);box-shadow:0 6px 28px rgba(0,0,0,.18);z-index:2}
.dev-item{position:absolute;left:0;width:520px}
.dev-icon{position:absolute;left:29px;width:84px;height:84px;border-radius:50%}
.dev-body{position:absolute;left:140px;width:300px}
.dev-body h4{font-size:12px;font-weight:600;color:#444}
.dev-body p{font-size:12px;line-height:17px;color:var(--grey);margin-top:13px}
.dev-body .more{display:block;font-size:11px;color:var(--grey);margin-top:12px;text-decoration:none}
.dev-link{left:140px;top:385px;font-size:12px;font-weight:600;color:#444;text-decoration:none;border-bottom:1px solid #999;padding-bottom:1px}

/* CTA band */
.cta{left:0;top:1814px;width:1200px;height:192px;background:linear-gradient(90deg,#e3e1dc 0%,#eeeeee 45%,#dfe3e6 100%)}
.cta-text{left:131px;top:1878px;font-size:23px;font-weight:500;line-height:27px;color:#1c1c1c}
.btn-submit{left:927px;top:1888px;width:137px;height:44px;font-size:15px;font-weight:600}

/* Gallery */
.gallery{left:133px;top:2046px;width:934px;height:186px;display:flex;gap:2px}
.gallery-tile{flex:1;height:186px}

.handle{left:0;top:2268px;width:1200px;text-align:center;font-size:24px;font-weight:600;color:#4a4a4a}

/* Footer */
.site-footer{left:7px;top:2334px;width:1186px;height:191px;background:var(--footer)}
.footer-nav{left:0;top:43px;width:1186px;text-align:center;font-size:12.5px;color:#555}
.footer-nav a{color:#555;text-decoration:none}
.footer-nav .sep{margin:0 6px}
.copyright{left:0;top:77px;width:1186px;text-align:center;font-size:11.5px;color:#666}
.social{left:544px;top:113px;display:flex;gap:16px}
.social a{width:15px;height:15px;border-radius:50%;background:#3d80c4;display:block}
</style>
</head>
<body>

<header class="site-header abs">
  <div class="brand abs">
    <span class="brand-mark"></span>
    <span class="brand-name">TIKO MARSDEN</span>
  </div>
  <nav class="main-nav">
    <a style="left:537px">FEATURES</a>
    <a style="left:643px">PLANS &amp; PRICING</a>
    <a style="left:798px">SERVICES</a>
    <a style="left:902px">LOGIN</a>
  </nav>
  <a class="btn btn-signup abs">SIGN UP</a>
</header>

<section class="hero abs" role="img" aria-label="Blurred office backdrop with a hand tapping a tablet and outlined envelopes flying out of it"></section>
<h1 class="hero-title abs">Email Marketing<br>Software</h1>
<p class="hero-tagline abs">It’s so easy a baby can use it!</p>
<p class="hero-sub abs">Simplify your email marketing now.</p>
<a class="btn btn-pricing abs">GET ACCESS TO PRICING</a>

<h2 class="intro-title abs">Where Teams Create and Send Beautiful Emails</h2>
<p class="intro-text abs">Our intuitive drag-and-drop editor makes designing the perfect email faster<br>with real-time collaboration and in-app commenting</p>

<div class="feature abs" style="left:108px;top:850px">
  <div class="feature-art" role="img" aria-label="Illustration of a team member with tools and gears" style="background:linear-gradient(135deg,#5fc3d6,#f0a35a)"></div>
  <h3>Collaborate with your team</h3>
  <p>Invite your team members on your account, give them specific roles &amp; permissions and collaborate together</p>
</div>
<div class="feature abs" style="left:446px;top:850px">
  <div class="feature-art" role="img" aria-label="Illustration of a segmentation flow chart on a pink circle" style="background:linear-gradient(135deg,#ee9a9a,#f4c6b4)"></div>
  <h3 style="margin-top:38px">Target specific contacts</h3>
  <p>Segment a specific portion of your lists according to their behaviour or contact informations and dynamically personalize your emails accordingly.</p>
</div>
<div class="feature abs" style="left:788px;top:840px">
  <div class="feature-art" role="img" aria-label="Illustration of a computer screen with charts for split testing" style="border-radius:8px;background:linear-gradient(135deg,#2b7fb3,#f06a5a)"></div>
  <h3 style="margin-top:36px">A/B test your campaigns</h3>
  <p>Test up to 10 versions of your emails to a portion of your list and send the version that will generate the best engagement.</p>
</div>

<h2 class="dev-title abs">Complete Solutions<br>For Developers</h2>
<div class="dev-photo abs" role="img" aria-label="Woman at a desk working on a computer showing a marketing screen"></div>
<div class="dev-card abs">
  <div class="dev-item" style="top:33px">
    <div class="dev-icon" role="img" aria-label="API icon" style="top:0;background:#3f4a55"></div>
    <div class="dev-body" style="top:12px">
      <h4>Powerful APIs</h4>
      <p>Integrating with our Send API is fast and simple. Send your first email in just a few minutes, with the programming language of your choice.</p>
      <a class="more">Learn More ›</a>
    </div>
  </div>
  <div class="dev-item" style="top:154px">
    <div class="dev-icon" role="img" aria-label="SMTP relay icon" style="top:0;background:#f27b5a"></div>
    <div class="dev-body" style="top:-3px">
      <h4>SMTP Relay</h4>
      <p>Postquill’s SMTP Server integrates easily with any system and scales with your volume needs.</p>
      <a class="more">Learn More ›</a>
    </div>
  </div>
  <div class="dev-item" style="top:260px">
    <div class="dev-icon" role="img" aria-label="Transactional SMS icon" style="top:0;background:#f7c948"></div>
    <div class="dev-body" style="top:-5px">
      <h4>Transactional SMS</h4>
      <p>Easily send text messages to your users around the globe through a simple RESTful API.</p>
      <a class="more">Learn More ›</a>
    </div>
  </div>
  <a class="dev-link abs">More about TIKO Email</a>
</div>

<section class="cta abs" role="img" aria-label="Soft blurred office backdrop"></section>
<p class="cta-text abs">Learn how easy it is to boost your business<br>with our email marketing software today.</p>
<a class="btn btn-submit abs">Submit Now</a>

<div class="gallery abs">
  <div class="gallery-tile" role="img" aria-label="Two colleagues looking at a phone" style="background:linear-gradient(135deg,#d9c7b3,#7a5b4d)"></div>
  <div class="gallery-tile" role="img" aria-label="Man thinking at a laptop" style="background:linear-gradient(135deg,#e4e4e4,#8a8f94)"></div>
  <div class="gallery-tile" role="img" aria-label="Hands holding a person icon on a dark network background" style="background:linear-gradient(135deg,#1f3449,#4f6a85)"></div>
  <div class="gallery-tile" role="img" aria-label="Business people discussing documents" style="background:linear-gradient(135deg,#cfd6dc,#4b5a6a)"></div>
  <div class="gallery-tile" role="img" aria-label="Woman working at a laptop with flowers on the desk" style="background:linear-gradient(135deg,#e8e3dd,#b89a6e)"></div>
</div>

<p class="handle abs">@Tiko Marsden Systems</p>

<footer class="site-footer abs">
  <nav class="footer-nav abs">
    <a>Features</a><span class="sep">|</span><a>Plans &amp; Pricing</a><span class="sep">|</span><a>API</a><span class="sep">|</span><a>About Us</a><span class="sep">|</span><a>Our Company</a><span class="sep">|</span><a>Blog</a><span class="sep">|</span><a>Contact Us</a><span class="sep">|</span><a>Support</a>
  </nav>
  <p class="copyright abs">Copyright © 2018 Tiko Marsden | All right reserved</p>
  <div class="social abs">
    <a aria-label="Social link"></a><a aria-label="Social link"></a><a aria-label="Social link"></a><a aria-label="Social link"></a>
  </div>
</footer>

</body>
</html>
```